Pack - Adventurous, Fun, Exciting, Social Fitness Club needs a Webpage with attitude!

Pack... we're a fun, social, outdoor fitness club that needs not just a homepage designed for our website, but in the process a "personality" for our unique, innovative and cheeky brand.
We pride ourselves on getting our members outdoors trying new, exciting physical activities in an effort to find joy in an active lifestyle, and sharing that experience with other like minded people. We offer:
- Personal Training (1-on-1 Fitness Training)
- Group Fitness Classes (Boxing, Pilates, etc)
- Boot Camps (Military Style - Sandbags, Ropes, Tyres, etc)
- Events (Fun Runs, Triathlons, Ocean Swims, Treks, etc)
- Adventures(Quorra Ridge Trek, Rock Climbing, Kayaking, etc)
Our tag line is 'No Judgements. No Limits!' The homepage should be exciting, adventurous and innovative, illustrating the values of our brand: possibility, thirst for life, personal accomplishment & freedom. It should be fun, friendly & inviting.
A few of our key benefits to members are:
- No Boring Workouts
- No Joining Fees or Long Term Contracts
- Results Guaranteed
The links below should give you a rough idea of the sort of "feel" we're after (vibrant, active, adventurous ).
http://www.campusroamer.com.au/
http://www.layoutgoblin.com/website-templates/31924.html
http://www.layoutgoblin.com/website-templates/32751.html
http://www.velmora.com/
Target Market(s)
Real, Everyday People - Men & Women (30:70) aged mainly between 21-40, who want a more exciting and enjoyable fitness experience than your typical gym offers.
Industry/Entity Type
Fitness
Requirements
Must have
- Strong, uplifting and motivating images of people enjoying fitness/physical activities outdoors

```html
<!DOCTYPE html>
<html lang="en">
<head>
<meta charset="utf-8">
<title>Pack – No Judgements. No Limits!</title>
<link rel="stylesheet" href="https://fonts.googleapis.com/css2?family=Bowlby+One&family=Cabin+Sketch:wght@700&family=Chewy&family=Paytone+One&family=Rubik+Dirt&display=swap">
<style>
  :root {
    --sun: #ffe800;
    --ember: #e3321f;
    --ink: #0a0a0a;
    --paper: #ffffff;
    --panel-top: #f26a00;
    --panel-bottom: #e02a00;
    --footer: #d02414;
    --frame-red: #e8301a;
  }
  * { margin: 0; padding: 0; box-sizing: border-box; }
  html, body { width: 1200px; height: 1200px; overflow: hidden; }
  body {
    position: relative;
    background: var(--sun);
    font-family: Arial, Helvetica, sans-serif;
    color: var(--ink);
  }

  /* Header */
  .top-stripe {
    position: absolute; left: 290px; right: 0; top: 94px; height: 26px;
    background: var(--ember);
  }
  .brand {
    position: absolute; left: 60px; top: 78px;
    display: flex; align-items: center; gap: 14px;
  }
  .brand-mark { width: 22px; height: 22px; background: var(--ember); }
  .brand-name {
    font-family: "Bowlby One", sans-serif; font-size: 58px; line-height: 1;
    color: var(--ink); letter-spacing: 1px;
  }
  .main-nav {
    position: absolute; top: 118px; left: 346px;
    display: flex; gap: 18px; list-style: none;
  }
  .main-nav a {
    display: block; width: 126px; height: 29px;
    background: var(--ink); color: var(--paper); border-radius: 5px;
    font-family: "Chewy", sans-serif; font-size: 22px; line-height: 27px;
    text-align: center; text-decoration: none; letter-spacing: 0.5px;
  }

  /* Hero */
  .hero {
    position: absolute; left: 0; top: 202px; width: 1200px; height: 460px;
    background: var(--ink);
  }
  .tagline {
    position: absolute; right: 714px; top: 345px; text-align: right;
    font-family: "Cabin Sketch", sans-serif; font-weight: 700;
    color: var(--sun); font-size: 62px; line-height: 1; letter-spacing: 2px;
  }
  .tagline-line { display: block; position: relative; }
  .tagline-line + .tagline-line { margin-top: 62px; }
  .tagline-no {
    position: absolute; right: -8px; top: -52px; font-size: 46px;
    transform: rotate(-8deg);
  }
  .photo-back {
    position: absolute; left: 532px; top: 190px; width: 540px; height: 488px;
    background: var(--frame-red); transform: rotate(-2.5deg);
  }
  .photo-frame {
    position: absolute; left: 540px; top: 196px; width: 560px; height: 470px;
    background: var(--sun); transform: rotate(1.5deg);
  }
  .hero-photo {
    position: absolute; left: 534px; top: 190px; width: 560px; height: 484px;
    transform: rotate(1deg);
    background: linear-gradient(100deg, #3a3a36 0%, #e9f1f0 14%, #ffffff 45%, #cfe0de 75%, #2c2a28 92%);
  }

  /* Benefits panel */
  .benefits {
    position: absolute; left: 30px; top: 662px; width: 1144px; height: 466px;
    background: linear-gradient(180deg, var(--panel-top) 0%, var(--panel-bottom) 100%);
    border-radius: 0 0 14px 14px;
  }
  .benefits-title {
    position: absolute; left: 66px; top: 682px;
    font-family: "Rubik Dirt", sans-serif; font-size: 42px; font-weight: 400;
    color: var(--ink);
  }
  .benefit-list { list-style: none; }
  .benefit {
    position: absolute; display: flex; align-items: center; gap: 8px;
    font-size: 26px; text-transform: uppercase; color: var(--ink);
  }
  .benefit svg { width: 40px; height: 22px; flex: none; }
  .benefit-1 { left: 86px;  top: 746px; }
  .benefit-2 { left: 128px; top: 818px; }
  .benefit-3 { left: 184px; top: 890px; }
  .services {
    position: absolute; left: 104px; top: 1000px; width: 1080px;
    font-family: "Paytone One", sans-serif; font-size: 31px; line-height: 1.35;
    text-transform: uppercase; color: var(--ink);
    transform: rotate(-2deg); transform-origin: left top;
  }

  /* Footer */
  .site-footer {
    position: absolute; left: 0; top: 1150px; width: 1200px; height: 50px;
    background: var(--footer);
  }
  .footer-links { list-style: none; }
  .footer-links li {
    position: absolute; top: 1170px; font-size: 20px; color: var(--ink);
    text-transform: uppercase;
  }
  .footer-links a { color: inherit; text-decoration: none; }
</style>
</head>
<body>
  <header>
    <div class="top-stripe"></div>
    <div class="brand">
      <span class="brand-mark"></span>
      <span class="brand-name">PACK</span>
    </div>
    <nav>
      <ul class="main-nav">
        <li><a href="#">about us</a></li>
        <li><a href="#">events</a></li>
        <li><a href="#">classes</a></li>
        <li><a href="#">boot camps</a></li>
        <li><a href="#">adventures</a></li>
        <li><a href="#">1-on-1</a></li>
      </ul>
    </nav>
  </header>

  <section class="hero-section">
    <div class="hero"></div>
    <h1 class="tagline">
      <span class="tagline-line"><span class="tagline-no">NO</span>JUDGEMENTS.</span>
      <span class="tagline-line"><span class="tagline-no">NO</span>LIMITS!</span>
    </h1>
    <div class="photo-back"></div>
    <div class="photo-frame"></div>
    <div class="hero-photo" role="img" aria-label="Kayaker in a green kayak dropping down a white-water waterfall between dark rocks"></div>
  </section>

  <section class="benefits-section">
    <div class="benefits"></div>
    <h2 class="benefits-title">WHY PACK?</h2>
    <ul class="benefit-list">
      <li class="benefit benefit-1">
        <svg viewBox="0 0 40 22" aria-hidden="true"><path d="M2 2h9l10 9-10 9H2l10-9z M18 2h9l10 9-10 9h-9l10-9z" fill="#0a0a0a"/></svg>
        No boring workouts
      </li>
      <li class="benefit benefit-2">
        <svg viewBox="0 0 40 22" aria-hidden="true"><path d="M2 2h9l10 9-10 9H2l10-9z M18 2h9l10 9-10 9h-9l10-9z" fill="#0a0a0a"/></svg>
        No joining fees or long-term contracts
      </li>
      <li class="benefit benefit-3">
        <svg viewBox="0 0 40 22" aria-hidden="true"><path d="M2 2h9l10 9-10 9H2l10-9z M18 2h9l10 9-10 9h-9l10-9z" fill="#0a0a0a"/></svg>
        Results guaranteed
      </li>
    </ul>
    <p class="services">Personal training, group fitness classes, military-style<br>boot camps, events, adventures and more</p>
  </section>

  <footer>
    <div class="site-footer"></div>
    <ul class="footer-links">
      <li style="left:268px"><a href="#">Site map</a></li>
      <li style="left:419px"><a href="#">Contact</a></li>
      <li style="left:594px"><a href="#">Other</a></li>
      <li style="left:716px">Design © 2011 Pack</li>
    </ul>
  </footer>
</body>
</html>
```